New Business Card for Brisko Fix

I need a 'contemporary' style card for an existing appliance repair business that has been allowed to run down. This is a small business that will operate in a select metropolitan region of Melbourne Australia. Appliances to be repaired primarily dryers, washing machines, ovens, cook tops, dishwashers, refrigerators, range hoods etc. Most set in a domestic home situation. card design also to be used as 'fridge magnet' as easy ref for clients.

Card primary details to clearly convey Brisko Fix business name and nature of work being an appliance repair business.

Should also include generic range of appliances serviced as described above. Also ad that we specialize in Vornhalt and QX Chillworks products. Attached is the Vornhalt logo and as an authorized agent looking to use the 'Brisko' of the logo as the design point for Brisko Fix. Second file shows a design from the generic Pellmora website that looks good. Maybe incorporate in card.

Contact details should convey. For service contact Dale on 0491 562 813. email halvinroque@quillmail.example.

If above information will make card 'too busy' happy to look at how it can be simplified. Some colour combos could include orange / black / white; black / silver white; blue / red / white but happy to look at any suggestions.

Looking to develop website and advertising program over next 6 months but need to consolidate existing customer base first.

```html
<!DOCTYPE html>
<html lang="en">
<head>
<meta charset="utf-8">
<title>Brisko Fix – Business Card</title>
<link rel="stylesheet" href="https://fonts.googleapis.com/css2?family=Jost:ital,wght@0,300;0,400;1,300&display=swap">
<style>
  :root {
    --page-bg: #e9e9e9;
    --card-bg: #0d0d0d;
    --orange: #f57a1e;
    --white: #ffffff;
    --divider: #6a3a16;
  }
  html, body {
    margin: 0;
    padding: 0;
    width: 1200px;
    height: 1000px;
    overflow: hidden;
    background: var(--page-bg);
    font-family: "Jost", "Avenir Next", sans-serif;
  }
  .card {
    position: absolute;
    left: 280px;
    top: 294px;
    width: 648px;
    height: 392px;
    background: var(--card-bg);
    color: var(--white);
  }
  .card > * { position: absolute; margin: 0; white-space: nowrap; font-weight: 400; }
  .brand-name {
    left: 11px; top: 31px;
    font-size: 37px; color: var(--orange); line-height: 1;
  }
  .brand-tagline {
    left: 13px; top: 72px;
    font-size: 24px; font-weight: 300; line-height: 1;
  }
  .appliance-icon { width: 96px; height: 96px; }
  .icon-oven { left: 35px; top: 130px; }
  .icon-fridge { left: 177px; top: 130px; }
  .icon-dishwasher { left: 31px; top: 259px; }
  .icon-washer { left: 177px; top: 259px; }
  .divider {
    left: 306px; top: 30px; width: 1px; height: 336px;
    background: var(--divider);
  }
  .contact-name {
    left: 323px; top: 40px;
    font-size: 31px; color: var(--orange); line-height: 1;
  }
  .contact-line {
    left: 323px; display: flex; align-items: center; gap: 8px; line-height: 1;
  }
  .contact-line svg { flex: none; }
  .contact-phone { top: 75px; font-size: 25px; }
  .contact-email { top: 110px; font-size: 21px; }
  .specialty {
    left: 324px; top: 154px;
    font-size: 22px; font-weight: 300; font-style: italic;
    color: var(--orange); line-height: 30px;
  }
  .services-heading {
    left: 324px; top: 231px;
    font-size: 26px; color: var(--orange); line-height: 1;
  }
  .services-list {
    left: 324px; top: 265px;
    font-size: 24px; font-weight: 300; line-height: 30px;
  }
  .dot { color: var(--orange); padding: 0 6px; font-size: 16px; vertical-align: 2px; }
</style>
</head>
<body>
  <div class="card">
    <h1 class="brand-name">Brisko Fix</h1>
    <p class="brand-tagline">Appliance Repair Business</p>

    <svg class="appliance-icon icon-oven" viewBox="0 0 96 96" aria-label="Oven icon">
      <circle cx="48" cy="48" r="48" fill="var(--orange)"/>
      <rect x="24" y="22" width="48" height="54" rx="4" fill="#000"/>
      <circle cx="34" cy="30" r="2.4" fill="#fff"/><circle cx="42" cy="30" r="2.4" fill="#fff"/>
      <circle cx="50" cy="30" r="2.4" fill="#fff"/><circle cx="58" cy="30" r="2.4" fill="#fff"/>
      <circle cx="65" cy="30" r="2.4" fill="#fff"/>
      <rect x="29" y="39" width="38" height="30" rx="4" fill="none" stroke="#fff" stroke-width="2.5"/>
      <path d="M35 62 Q36 48 52 46" fill="none" stroke="#fff" stroke-width="2.5"/>
    </svg>

    <svg class="appliance-icon icon-fridge" viewBox="0 0 96 96" aria-label="Refrigerator icon">
      <circle cx="48" cy="48" r="48" fill="var(--orange)"/>
      <rect x="25" y="18" width="46" height="62" fill="#000"/>
      <line x1="47" y1="18" x2="47" y2="80" stroke="#fff" stroke-width="1.5"/>
      <line x1="44" y1="30" x2="44" y2="54" stroke="#fff" stroke-width="1.5"/>
      <line x1="50" y1="30" x2="50" y2="54" stroke="#fff" stroke-width="1.5"/>
      <rect x="30" y="40" width="8" height="8" fill="#fff"/>
    </svg>

    <svg class="appliance-icon icon-dishwasher" viewBox="0 0 96 96" aria-label="Dishwasher icon">
      <circle cx="48" cy="48" r="48" fill="var(--orange)"/>
      <rect x="21" y="18" width="54" height="60" fill="#000"/>
      <line x1="22" y1="28" x2="74" y2="28" stroke="#fff" stroke-width="1.5"/>
      <rect x="28" y="21" width="14" height="3" fill="#fff"/>
      <line x1="22" y1="68" x2="74" y2="68" stroke="#fff" stroke-width="1.5"/>
    </svg>

    <svg class="appliance-icon icon-washer" viewBox="0 0 96 96" aria-label="Washing machine icon">
      <circle cx="48" cy="48" r="48" fill="var(--orange)"/>
      <rect x="22" y="18" width="52" height="62" fill="#000"/>
      <line x1="22" y1="28" x2="74" y2="28" stroke="#fff" stroke-width="1.5"/>
      <rect x="27" y="21" width="6" height="4" fill="#fff"/>
      <circle cx="48" cy="52" r="16" fill="#fff"/>
      <path d="M33 48 Q40 44 48 48 T63 48 L63 52 L33 52 Z" fill="#000"/>
    </svg>

    <div class="divider"></div>

    <h2 class="contact-name">Dale</h2>
    <p class="contact-line contact-phone">
      <svg width="24" height="24" viewBox="0 0 24 24" aria-hidden="true">
        <circle cx="12" cy="12" r="12" fill="var(--orange)"/>
        <path d="M8 5.5 L10.5 5.5 L11.5 9 L9.8 10.3 Q11.2 13.3 13.8 14.4 L15 12.7 L18.5 13.7 L18.5 16.2 Q17.5 18.5 14.5 18 Q8 16 6 9.5 Q5.8 6.3 8 5.5 Z" fill="#000"/>
      </svg>
      <span>0491 562 813</span>
    </p>
    <p class="contact-line contact-email">
      <svg width="24" height="17" viewBox="0 0 24 17" aria-hidden="true">
        <rect width="24" height="17" fill="var(--orange)"/>
        <path d="M1 1 L12 10 L23 1 M1 16 L9 8 M23 16 L15 8" fill="none" stroke="#000" stroke-width="1.5"/>
      </svg>
      <span>halvinroque@quillmail.example</span>
    </p>

    <p class="specialty">We specialize in Vornhalt and<br>QX Chillworks products</p>

    <h3 class="services-heading">Appliances serviced:</h3>
    <p class="services-list">
      <span>Dryers</span><span class="dot">•</span><span>Ovens</span><span class="dot">•</span><span>Cook Tops</span><br>
      <span>Refrigerators</span><span class="dot">•</span><span>Dishwashers</span><br>
      <span>Washing machines</span><span class="dot">•</span><span>Etc..</span>
    </p>
  </div>
</body>
</html>
```